Business Card Design Project

I would like a business card created for a new company. This is a holding company that acts as my investment company. It holds real estate and service based companies. The name of the company is Sandorecca which is Italian for Evolution. Defined as development or growth.
We currently have no logo. I really like some of the "different" cards out there. Potentially metallic or grey/black. That looks premium/hi-end and unique. I am not sure if your design would be specific to the card stock I end with our just logo/design/font.
Real Estate

```html
<!DOCTYPE html>
<html lang="en">
<head>
<meta charset="utf-8">
<title>Sandorecca Business Card</title>
<link rel="stylesheet" href="https://fonts.googleapis.com/css2?family=Cinzel:wght@400;500&display=swap">
<style>
  :root {
    --page: #ffffff;
    --ink: #0d0d0d;
    --metal-deep: #0e0e0e;
    --metal-dark: #4a4a4a;
    --metal-mid: #a8a8a8;
    --metal-light: #e6e6e6;
    --metal-shine: #ffffff;
    --metal-edge: #2a2a2a;
  }
  html, body {
    margin: 0;
    padding: 0;
    width: 1200px;
    height: 754px;
    overflow: hidden;
    background: var(--page);
  }
  .canvas {
    position: relative;
    width: 1200px;
    height: 754px;
  }
  .card {
    position: absolute;
    left: 26px;
    top: 24px;
    width: 1150px;
    height: 702px;
    border-radius: 34px;
    overflow: hidden;
    background: linear-gradient(58deg,
      var(--metal-deep) 0%,
      var(--metal-dark) 22%,
      var(--metal-mid) 44%,
      var(--metal-light) 58%,
      var(--metal-shine) 68%,
      var(--metal-light) 76%,
      var(--metal-dark) 90%,
      var(--metal-edge) 100%);
    font-family: "Cinzel", serif;
    color: var(--ink);
  }
  .brand-name {
    position: absolute;
    left: 70px;
    top: 172px;
    margin: 0;
    font-size: 66px;
    font-weight: 500;
    letter-spacing: 4px;
    line-height: 1;
  }
  .holder-name {
    position: absolute;
    left: 0;
    right: 0;
    top: 352px;
    margin: 0;
    text-align: center;
    font-size: 78px;
    font-weight: 400;
    letter-spacing: 6px;
    line-height: 1;
    text-shadow: 1px 2px 2px rgba(0, 0, 0, 0.35);
  }
  .contact {
    position: absolute;
    left: 433px;
    top: 582px;
    margin: 0;
    font-size: 31px;
    letter-spacing: 3px;
    line-height: 54px;
    font-style: normal;
  }
  .contact-line {
    display: block;
  }
</style>
</head>
<body>
  <div class="canvas">
    <section class="card" aria-label="Sandorecca business card">
      <h1 class="brand-name">Sandorecca</h1>
      <h2 class="holder-name">Your Name</h2>
      <address class="contact">
        <span class="contact-line">Phone:5555-5555</span>
        <span class="contact-line">Email; info@sandorecca.com</span>
      </address>
    </section>
  </div>
</body>
</html>
```